Harbor Lantern Vodka needs new design for its Chili Vodka line

use the existing label attached to add a chili aspect to the label for our new Chili Vodka.

Target Market(s)

high end

Requirements
Must have
• creative image
Nice to have
• red chili peppers
Should not have
• fire

```html
<!DOCTYPE html>
<html lang="en">
<head>
<meta charset="utf-8">
<title>Harbor Lantern Vodka – Red Chili Peppers Label</title>
<link rel="stylesheet" href="https://fonts.googleapis.com/css2?family=Barlow+Semi+Condensed:wght@500;600&family=Barlow+Condensed:wght@500;600&display=swap">
<style>
  :root {
    --page: #ffffff;
    --label: #ffffff;
    --gold: #d49a2c;
    --gold-light: #f1c560;
    --ink: #1c1c1c;
    --band-red: #8e1111;
    --band-text: #ffffff;
    --chili-red: #d51a10;
    --chili-dark: #a80f0a;
    --chili-seed: #f3dcc0;
  }
  * { margin: 0; padding: 0; box-sizing: border-box; }
  html, body {
    width: 960px;
    height: 1200px;
    overflow: hidden;
    background: var(--page);
  }
  .canvas {
    position: relative;
    width: 960px;
    height: 1200px;
    background: var(--page);
  }
  .label {
    position: absolute;
    left: 130px;
    top: 105px;
    width: 700px;
    height: 990px;
    background: var(--label);
    box-shadow: 0 0 0 1px #ececec;
  }
  .label__frame {
    position: absolute;
    inset: 12px;
    border: 3px solid var(--gold);
  }
  .distillery {
    position: absolute;
    top: 54px;
    left: 0;
    width: 100%;
    text-align: center;
    font-family: "Barlow Semi Condensed", sans-serif;
    font-weight: 500;
    font-size: 19px;
    letter-spacing: 0.5px;
    color: var(--ink);
  }
  .wordmark {
    position: absolute;
    top: 118px;
    left: 90px;
    width: 520px;
    font-family: "Barlow Semi Condensed", sans-serif;
    font-weight: 600;
    color: var(--gold);
    text-align: center;
    line-height: 0.95;
    text-transform: uppercase;
  }
  .wordmark__line { display: block; }
  .wordmark__line--harbor { font-size: 128px; }
  .wordmark__line--lantern { font-size: 128px; }
  .wordmark__line--vodka { font-size: 128px; }
  .tagline {
    position: absolute;
    top: 606px;
    left: 0;
    width: 100%;
    text-align: center;
    font-family: "Barlow Semi Condensed", sans-serif;
    font-weight: 500;
    font-size: 21px;
    letter-spacing: 3px;
    color: var(--ink);
  }
  .chili-image {
    position: absolute;
    left: 71px;
    top: 680px;
    width: 562px;
    height: 150px;
    border-radius: 75px 60px 60px 90px / 60px 70px 70px 80px;
    background: linear-gradient(100deg, var(--chili-dark) 0%, var(--chili-red) 45%, #e8331b 75%, var(--chili-dark) 100%);
  }
  .spec-band {
    position: absolute;
    left: 44px;
    top: 883px;
    width: 613px;
    height: 73px;
    background: var(--band-red);
    border-top: 3px solid var(--gold);
    border-bottom: 3px solid var(--gold);
    display: flex;
    align-items: center;
    color: var(--band-text);
    font-family: "Barlow Condensed", sans-serif;
    font-weight: 600;
  }
  .spec-band__abv {
    width: 118px;
    text-align: center;
    line-height: 1;
  }
  .spec-band__abv-value { display: block; font-size: 26px; }
  .spec-band__abv-unit { display: block; font-size: 18px; font-weight: 500; }
  .spec-band__divider {
    width: 2px;
    height: 48px;
    background: var(--band-text);
  }
  .spec-band__flavour {
    flex: 1;
    text-align: center;
    font-size: 36px;
    letter-spacing: 0.5px;
  }
  .spec-band__volume {
    width: 110px;
    text-align: center;
    font-size: 34px;
  }
</style>
</head>
<body>
  <main class="canvas">
    <section class="label">
      <div class="label__frame"></div>
      <p class="distillery">GREYWATER DISTILLERY</p>
      <h1 class="wordmark">
        <span class="wordmark__line wordmark__line--harbor">Harbor</span>
        <span class="wordmark__line wordmark__line--lantern">Lantern</span>
        <span class="wordmark__line wordmark__line--vodka">Vodka</span>
      </h1>
      <p class="tagline">PREMIUM QUALITY</p>
      <div class="chili-image" role="img" aria-label="Photograph of a halved red chili pepper with seeds and green stem"></div>
      <div class="spec-band">
        <div class="spec-band__abv">
          <span class="spec-band__abv-value">40%</span>
          <span class="spec-band__abv-unit">Alc/Vol</span>
        </div>
        <div class="spec-band__divider"></div>
        <div class="spec-band__flavour">RED CHILI PEPPERS</div>
        <div class="spec-band__divider"></div>
        <div class="spec-band__volume">70cl</div>
      </div>
    </section>
  </main>
</body>
</html>
```